Business Card Design for Tax Accounting Company

I need design files that can be edited to add new professional designations onto the end of my name once complete. I need design files that can be edited for new employees. I also need the design files to be able to upload into CardNest for new orders. I've attached multiple logo files with varying file extensions to help with the design.
Please include the following contact information:
Marcus Tellan, CFP®, EA, CTC, CEPA
Founder & CEO
C (480) 517.3082
F (623) 389.5170
718 W Larkspur Ave
Mesa, AZ 85210
Updates
I need the business card to include the following contact info:
C: (480)517.3082
F: (623) 389.5170
mt@RidgewayLedgerGroup.com
www.MarcusRTellan.com
Address to be included is
718 W Larkspur Ave
Mesa, AZ 85210
Business Cards are double sided
Target Market(s)
Business owners $1M+ annual revenue, especially for the construction and technology industries
Industry/Entity Type
Accounting & Tax
Contact Information for Business Card
Contact information and logo
Look and feel
Each slider illustrates characteristics of the customer's brand and the style your logo design should communicate.

```html
<!DOCTYPE html>
<html lang="en">
<head>
<meta charset="utf-8">
<title>Ridgeway Ledger Group – Business Card</title>
<link href="https://fonts.googleapis.com/css2?family=Tinos:wght@400;700&display=swap" rel="stylesheet">
<style>
  :root {
    --navy: #232f6e;
    --orange: #d15f24;
    --red: #be1e2d;
    --yellow: #fcd406;
    --paper: #ffffff;
    --mist: #efefef;
    --backdrop: #2b2b2b;
  }
  * { box-sizing: border-box; margin: 0; padding: 0; }
  html, body { width: 1200px; height: 900px; overflow: hidden; }
  body {
    background: var(--backdrop);
    font-family: "Tinos", "Times New Roman", serif;
    position: relative;
  }
  .card {
    position: absolute;
    left: 250px;
    width: 700px;
    height: 400px;
    border-radius: 28px;
    overflow: hidden;
    background: var(--paper);
  }
  .card--front { top: 30px; }
  .card--back { top: 470px; }

  /* front */
  .sunburst-band {
    position: absolute;
    left: 0; right: 0;
    background: linear-gradient(90deg, var(--red), var(--yellow) 30%, var(--red) 55%, var(--yellow) 80%, var(--red));
  }
  .sunburst-band--top { top: 0; height: 110px; }
  .sunburst-band--bottom { bottom: 0; height: 120px; }
  .wordmark {
    position: absolute;
    display: flex;
    align-items: center;
    gap: 12px;
    color: var(--navy);
    font-weight: 700;
    white-space: nowrap;
  }
  .wordmark__dot {
    border-radius: 50%;
    background: var(--orange);
    flex: none;
  }
  .card--front .wordmark {
    left: 0; right: 0; top: 170px;
    justify-content: center;
    font-size: 40px;
  }
  .card--front .wordmark__dot { width: 34px; height: 34px; }

  /* back */
  .ray-field {
    position: absolute; inset: 0;
    background: radial-gradient(circle at 58% 42%, #ffffff 0%, var(--mist) 70%);
  }
  .accent-panel { position: absolute; inset: 0; }
  .card--back .wordmark {
    left: 50px; top: 160px;
    font-size: 30px;
  }
  .card--back .wordmark__dot { width: 26px; height: 26px; }
  .holder {
    position: absolute;
    right: 90px; top: 26px;
    font-size: 17px;
    font-weight: 700;
    color: var(--navy);
    white-space: nowrap;
  }
  .holder__credentials { color: var(--orange); }
  .address {
    position: absolute;
    left: 50px; top: 300px;
    display: flex; align-items: center; gap: 12px;
    color: var(--navy);
    font-size: 19px;
    line-height: 1.25;
  }
  .contact-list {
    position: absolute;
    right: 34px; top: 228px;
    list-style: none;
    color: var(--paper);
    font-size: 15px;
    text-align: right;
  }
  .contact-list li {
    display: flex; justify-content: flex-end; align-items: center;
    gap: 10px; height: 25px;
  }
  .contact-list svg { width: 16px; height: 16px; flex: none; }
</style>
</head>
<body>

<section class="card card--front" aria-label="Card front">
  <div class="sunburst-band sunburst-band--top" role="img" aria-label="Red and yellow sunburst rays"></div>
  <div class="wordmark"><span class="wordmark__dot"></span>Ridgeway Ledger Group</div>
  <div class="sunburst-band sunburst-band--bottom" role="img" aria-label="Red and yellow sunburst rays"></div>
</section>

<section class="card card--back" aria-label="Card back">
  <div class="ray-field" role="img" aria-label="Faint white rays on light grey"></div>
  <svg class="accent-panel" viewBox="0 0 700 400" preserveAspectRatio="none" aria-hidden="true">
    <polygon points="300,400 700,60 700,400" fill="var(--orange)"/>
    <line x1="282" y1="400" x2="682" y2="60" stroke="var(--navy)" stroke-width="12"/>
  </svg>

  <p class="holder">Marcus Tellan, <span class="holder__credentials">CFP®, EA, CTC, CEPA</span></p>

  <div class="wordmark"><span class="wordmark__dot"></span>Ridgeway Ledger Group</div>

  <div class="address">
    <svg width="20" height="26" viewBox="0 0 20 26" aria-hidden="true">
      <path d="M10 1a8 8 0 0 0-8 8c0 6 8 16 8 16s8-10 8-16a8 8 0 0 0-8-8z" fill="var(--navy)"/>
      <circle cx="10" cy="9" r="3.2" fill="var(--paper)"/>
    </svg>
    <p>718 W Larkspur Ave<br>Mesa, AZ 85210</p>
  </div>

  <ul class="contact-list">
    <li>(480)517.3082
      <svg viewBox="0 0 16 16" aria-hidden="true"><path d="M4 1l3 3-2 2c1 2 3 4 5 5l2-2 3 3-2 3C7 15 1 9 1 3z" fill="var(--paper)"/></svg>
    </li>
    <li>(623) 389.5170
      <svg viewBox="0 0 16 16" aria-hidden="true"><rect x="4" y="1" width="8" height="5" fill="var(--paper)"/><rect x="1" y="6" width="14" height="6" rx="1" fill="var(--paper)"/><rect x="4" y="10" width="8" height="5" fill="var(--paper)" stroke="var(--orange)"/></svg>
    </li>
    <li>mt@RidgewayLedgerGroup.com
      <svg viewBox="0 0 16 16" aria-hidden="true"><rect x="1" y="3" width="14" height="10" fill="var(--paper)"/><path d="M1 3l7 6 7-6" fill="none" stroke="var(--orange)" stroke-width="1.3"/></svg>
    </li>
    <li>www.MarcusRTellan.com
      <svg viewBox="0 0 16 16" aria-hidden="true"><g fill="none" stroke="var(--paper)" stroke-width="1.3"><circle cx="8" cy="8" r="6.5"/><ellipse cx="8" cy="8" rx="3" ry="6.5"/><path d="M1.5 8h13M2.5 4.5h11M2.5 11.5h11"/></g></svg>
    </li>
  </ul>
</section>

</body>
</html>
```